Fundraising team needing letterhead for sponsorship and donations

I would like a design that relates to our team name Purely the Ribbon. We ride in an annual bicycle event that raises money that goes towards cancer research.We already have a team jersey designed which i have attached. The team name we would prefer to be in pink. Our team includes males and females. The logo also needs to relate to bike riding.

Industry/Entity Type

Event

Font styles to use
Sans Serif

```html
<!DOCTYPE html>
<html lang="en">
<head>
<meta charset="utf-8">
<title>Purely the Ribbon – Letterhead</title>
<link href="https://fonts.googleapis.com/css2?family=Montserrat:wght@500;700;800&family=Dancing+Script:wght@600;700&display=swap" rel="stylesheet">
<style>
  :root {
    --pink: #e6157f;
    --pink-soft: #f7c6de;
    --pink-faint: #fbe3ef;
    --blue: #2a64b4;
    --blue-mid: #3b8fd8;
    --blue-light: #a9d3f3;
    --sky: #e3f1fb;
    --paper: #ffffff;
    --backdrop: #f2f2f2;
    --ink-white: #ffffff;
  }
  * { box-sizing: border-box; margin: 0; padding: 0; }
  html, body { width: 1200px; height: 1000px; overflow: hidden; }
  body {
    background: var(--backdrop);
    font-family: "Montserrat", Arial, sans-serif;
    position: relative;
  }
  .letterhead {
    position: absolute;
    left: 264px; top: 30px;
    width: 671px; height: 940px;
    background: var(--paper);
    overflow: hidden;
    box-shadow: 0 4px 18px rgba(0,0,0,.15);
  }
  .header-wave { position: absolute; left: 0; top: 0; width: 671px; height: 170px; }
  .brand {
    position: absolute; left: 34px; top: 34px;
    display: flex; align-items: center; gap: 14px;
    z-index: 2;
  }
  .brand-dot {
    width: 46px; height: 46px; border-radius: 50%;
    background: var(--pink-soft);
  }
  .brand-name {
    font-weight: 800; font-size: 30px; color: var(--pink);
    letter-spacing: .5px; white-space: nowrap;
  }
  .watermark {
    position: absolute; left: 0; right: 0; top: 400px;
    display: flex; flex-direction: column; align-items: center; gap: 18px;
  }
  .watermark-dot {
    width: 120px; height: 120px; border-radius: 50%;
    background: var(--pink-faint);
  }
  .watermark-name {
    font-weight: 800; font-size: 40px; color: var(--pink-faint);
    white-space: nowrap;
  }
  .footer-wave { position: absolute; left: 0; bottom: 40px; width: 671px; height: 130px; }
  .rider-band {
    position: absolute; left: 30px; right: 20px; bottom: 82px; height: 30px;
    background: linear-gradient(90deg, var(--blue) 0%, var(--blue-mid) 60%, var(--blue-light) 100%);
    border-radius: 6px; opacity: .85;
  }
  .tagline {
    position: absolute; left: 0; right: 0; bottom: 56px;
    text-align: center;
    font-family: "Dancing Script", cursive;
    font-weight: 700;
    font-size: 17px; line-height: 22px; color: var(--ink-white);
    text-shadow: 0 0 3px rgba(42,100,180,.9);
    white-space: nowrap;
    z-index: 2;
  }
  .contact-bar {
    position: absolute; left: 0; right: 0; bottom: 0; height: 52px;
    display: flex; font-size: 7px; font-weight: 700; line-height: 1.45;
    color: var(--ink-white); text-transform: uppercase; letter-spacing: .3px;
    z-index: 1;
  }
  .contact-address {
    width: 236px; background: var(--pink);
    padding: 0 14px 0 30px;
    display: flex; align-items: center;
  }
  .contact-details {
    flex: 1; background: var(--blue);
    display: flex; justify-content: space-around; align-items: center;
    padding: 0 8px;
  }
  .contact-item { display: flex; align-items: center; gap: 5px; white-space: nowrap; }
  .contact-item svg { width: 11px; height: 11px; flex: none; }
</style>
</head>
<body>
  <main class="letterhead">
    <svg class="header-wave" viewBox="0 0 671 170" preserveAspectRatio="none" aria-hidden="true">
      <defs>
        <linearGradient id="headBlue" x1="0" y1="0" x2="1" y2="0">
          <stop offset="0" stop-color="#7fc0ee"/>
          <stop offset=".6" stop-color="#3b8fd8"/>
          <stop offset="1" stop-color="#2a64b4"/>
        </linearGradient>
      </defs>
      <path d="M0 0 H671 V150 C560 80 430 70 300 60 C180 50 80 40 0 46 Z" fill="url(#headBlue)"/>
      <path d="M0 30 C150 20 330 45 480 70 C570 85 630 110 671 135" stroke="#e3f1fb" stroke-width="6" fill="none" opacity=".8"/>
      <path d="M60 10 C220 5 400 30 540 50 C600 60 650 75 671 85" stroke="#ffffff" stroke-width="3" fill="none" opacity=".6"/>
      <path d="M0 46 C80 40 180 50 300 60 C430 70 560 80 671 150 V170 C560 110 420 92 280 82 C160 74 60 70 0 72 Z" fill="#e3f1fb" opacity=".7"/>
    </svg>

    <div class="brand">
      <span class="brand-dot"></span>
      <span class="brand-name">Purely the Ribbon</span>
    </div>

    <div class="watermark">
      <span class="watermark-dot"></span>
      <span class="watermark-name">Purely the Ribbon</span>
    </div>

    <svg class="footer-wave" viewBox="0 0 671 130" preserveAspectRatio="none" aria-hidden="true">
      <defs>
        <linearGradient id="footBlue" x1="0" y1="0" x2="1" y2="0">
          <stop offset="0" stop-color="#3b8fd8"/>
          <stop offset="1" stop-color="#a9d3f3"/>
        </linearGradient>
      </defs>
      <path d="M0 40 C200 30 420 40 671 10 V130 H0 Z" fill="url(#footBlue)" opacity=".9"/>
      <path d="M0 60 C220 45 440 55 671 25" stroke="#ffffff" stroke-width="3" fill="none" opacity=".7"/>
    </svg>

    <div class="rider-band" role="img" aria-label="Row of cyclist silhouettes in shades of blue"></div>
    <p class="tagline">Fundraising Bike Ride for Cancer Research</p>

    <footer class="contact-bar">
      <div class="contact-address">Name of the organization, address line 1, address line 2, city &amp; zip code</div>
      <div class="contact-details">
        <span class="contact-item">
          <svg viewBox="0 0 12 12"><circle cx="6" cy="6" r="5.5" fill="none" stroke="#fff"/><path d="M4 3.2 L5 4.6 L4.5 5.2 C5 6.3 5.7 7 6.8 7.5 L7.4 7 L8.8 8 L8.2 9 C5.5 8.8 3.2 6.5 3 3.8 Z" fill="#fff"/></svg>
          0400 555 0199
        </span>
        <span class="contact-item">
          <svg viewBox="0 0 12 12"><circle cx="6" cy="6" r="5.5" fill="none" stroke="#fff"/><ellipse cx="6" cy="6" rx="2.2" ry="4.5" fill="none" stroke="#fff" stroke-width=".8"/><path d="M1.5 6 H10.5" stroke="#fff" stroke-width=".8"/></svg>
          www.purelytheribbon.org.au
        </span>
        <span class="contact-item">
          <svg viewBox="0 0 12 12"><circle cx="6" cy="6" r="5.5" fill="none" stroke="#fff"/><rect x="3" y="4" width="6" height="4.2" fill="none" stroke="#fff" stroke-width=".8"/><path d="M3 4 L6 6.5 L9 4" stroke="#fff" stroke-width=".8" fill="none"/></svg>
          info@purelytheribbon.org.au
        </span>
      </div>
    </footer>
  </main>
</body>
</html>
```